ecommerce news podcast artwork

Podcast cover art for a podcast featuring daily news and events around ecommerce product businesses.

text to be: TILLWIRE
optional third line of text with smaller font: Podcast

looking for something that pops with a medium to light blue background. text can be in white/red/orange colors. prefer solid colors for text, but background can vary.
I'm really open to other ideas too, sometimes you don't know what you want until you see it.

Target Market(s)

ecommerce business owners, managers

Industry/Entity Type

news, business, ecommerce

Font styles to use
Sans Serif

Colors
0054AA
0677BA
7BADD7
CADEEF
E8F1F8
0094D4
00A9DD
6FCCEA
C7EBF8
E9F6FB
F0912C
F2A743
F7CA91
FBE8D2
FDF5EE
EB3D1F
EC4F4E
F09395
F8D3D4
FCEDEE

Requirements
Must have
• text: TILLWIRE
Should not have
• no microphones, headsets/headphones, speakers, or other props like that.

```html
<!DOCTYPE html>
<html lang="en">
<head>
<meta charset="utf-8">
<title>Tillwire Podcast Cover</title>
<link rel="stylesheet" href="https://fonts.googleapis.com/css2?family=Oswald:wght@600;700&display=swap">
<style>
  :root {
    --canvas-grey: #d1d3d5;
    --brand-blue: #0054aa;
    --brand-orange: #fa8a00;
    --text-white: #ffffff;
  }
  html, body {
    margin: 0;
    padding: 0;
    width: 1200px;
    height: 1200px;
    overflow: hidden;
    background: var(--canvas-grey);
  }
  .cover {
    display: block;
    width: 1200px;
    height: 1200px;
  }
  .cover__panel { fill: var(--brand-blue); }
  .cover__frame { fill: none; stroke: var(--brand-orange); stroke-width: 9.5; }
  .title {
    font-family: "Oswald", "Arial Narrow", sans-serif;
    font-weight: 700;
  }
  .title--top { fill: var(--text-white); font-size: 448px; }
  .title--bottom { fill: var(--brand-orange); font-size: 406px; }
  .label-pill { fill: var(--brand-orange); }
  .label-pill__text {
    font-family: "Oswald", "Arial Narrow", sans-serif;
    font-weight: 600;
    font-size: 47px;
    fill: var(--text-white);
  }
</style>
</head>
<body>
<svg class="cover" viewBox="0 0 1200 1200" xmlns="http://www.w3.org/2000/svg" role="img" aria-label="Tillwire Podcast cover art">
  <rect width="1200" height="1200" fill="var(--canvas-grey)"/>
  <rect class="cover__panel" x="68" y="68" width="1063" height="1063"/>
  <rect class="cover__frame" x="102.5" y="100" width="999" height="1002"/>

  <text class="title title--top" x="222" y="543" textLength="736" lengthAdjust="spacingAndGlyphs">TILL</text>
  <text class="title title--bottom" x="222" y="905" textLength="739" lengthAdjust="spacingAndGlyphs">WIRE</text>

  <rect class="label-pill" x="222" y="943" width="741" height="76" rx="38" ry="38"/>
  <text class="label-pill__text" x="347" y="999" textLength="442" lengthAdjust="spacing">PODCAST</text>
</svg>
</body>
</html>
```